packing for cake and sweet

we need packing design for cake box.
I attached some nice packing from other shop like :
Bruma and velmont for examples.

I attached the logo.
you can make packing with any colors you choose.

box size :
length : 30 cm
Width : 30 cm
Height : 15 cm

this shops have very good design :
https://www.quorvell.co.uk/hot-chocolate/discover-hot-chocolate/all-hot-chocolate

Industry/Entity Type

food

Font styles to use
Other font styles liked:
• same our logo already attached.

```html
<!DOCTYPE html>
<html lang="en">
<head>
<meta charset="utf-8">
<title>Vaudelle cake box dieline</title>
<link rel="stylesheet" href="https://fonts.googleapis.com/css2?family=Cinzel:wght@400&display=swap">
<style>
  :root {
    --page-bg: #ffffff;
    --box-violet: #2e2079;
    --violet-mid: #2f2a80;
    --ornament-blue: #2f4b96;
    --ornament-soft: rgba(52, 84, 160, 0.38);
    --fold-line: #9a93cf;
    --brand-white: #ffffff;
    --panel: 262px;
    --flap: 131px;
  }
  * { margin: 0; padding: 0; box-sizing: border-box; }
  html, body {
    width: 1200px;
    height: 526px;
    overflow: hidden;
    background: var(--page-bg);
  }
  .canvas {
    position: relative;
    width: 1200px;
    height: 526px;
    background: var(--page-bg);
  }
  .dieline {
    position: absolute;
    left: 337px;
    top: 0;
    width: 525px;
    height: 525px;
  }
  .face {
    position: absolute;
    overflow: hidden;
    background: var(--box-violet);
    display: flex;
    align-items: center;
    justify-content: center;
  }
  .face-pattern {
    position: absolute;
    inset: 0;
    background:
      radial-gradient(circle at 0% 0%, var(--ornament-soft) 0%, transparent 38%),
      radial-gradient(circle at 100% 0%, var(--ornament-soft) 0%, transparent 38%),
      radial-gradient(circle at 0% 100%, var(--ornament-soft) 0%, transparent 38%),
      radial-gradient(circle at 100% 100%, var(--ornament-soft) 0%, transparent 38%),
      radial-gradient(circle at 50% 50%, var(--violet-mid) 0%, var(--box-violet) 30%, rgba(47, 75, 150, 0.45) 62%, var(--box-violet) 90%);
  }
  .face--lid    { left: var(--flap); top: var(--flap); width: var(--panel); height: var(--panel);
                  outline: 1px solid var(--fold-line); outline-offset: -1px; z-index: 2; }
  .face--back   { left: var(--flap); top: 0; width: var(--panel); height: var(--flap); }
  .face--front  { left: var(--flap); top: calc(var(--flap) + var(--panel)); width: var(--panel); height: var(--flap); }
  .face--left   { left: 0; top: var(--flap); width: var(--flap); height: var(--panel); }
  .face--right  { left: calc(var(--flap) + var(--panel)); top: var(--flap); width: var(--flap); height: var(--panel); }

  .brand-name {
    position: relative;
    font-family: "Cinzel", "Times New Roman", serif;
    font-weight: 400;
    font-size: 31px;
    letter-spacing: 0.5px;
    color: var(--brand-white);
    white-space: nowrap;
    line-height: 1;
  }
  .face--back  .brand-name { transform: rotate(180deg); }
  .face--left  .brand-name { transform: rotate(90deg); }
  .face--right .brand-name { transform: rotate(-90deg); }
</style>
</head>
<body>
  <main class="canvas">
    <section class="dieline" aria-label="Cake box net, 30 × 30 × 15 cm">
      <div class="face face--back">
        <div class="face-pattern" role="img" aria-label="Faint blue mandala ornament pattern on violet"></div>
        <p class="brand-name">Vaudelle</p>
      </div>
      <div class="face face--left">
        <div class="face-pattern" role="img" aria-label="Faint blue mandala ornament pattern on violet"></div>
        <p class="brand-name">Vaudelle</p>
      </div>
      <div class="face face--lid">
        <div class="face-pattern" role="img" aria-label="Large faint blue mandala ornament centred on the violet lid"></div>
        <p class="brand-name">Vaudelle</p>
      </div>
      <div class="face face--right">
        <div class="face-pattern" role="img" aria-label="Faint blue mandala ornament pattern on violet"></div>
        <p class="brand-name">Vaudelle</p>
      </div>
      <div class="face face--front">
        <div class="face-pattern" role="img" aria-label="Faint blue mandala ornament pattern on violet"></div>
        <p class="brand-name">Vaudelle</p>
      </div>
    </section>
  </main>
</body>
</html>
```